Business Card for Holistic Health Business
Bright Ferns Natural Wellness & Live Cell Review
Use same font as used in my logo
Not sure, I am open to different fonts.
Simple
Marla Dunwoody
DynBC, CH, BA
Larkvale Acupuncture Clinic
2736-18 Avenue, Suite 200
Larkvale, AB T8K 2P6
brightferns@mailnest.ca
www.brightfernsnaturalwellness.com
Logo for Bright Ferns business card.

```html
<!DOCTYPE html>
<html lang="en">
<head>
<meta charset="utf-8">
<title>Bright Ferns Business Card</title>
<link href="https://fonts.googleapis.com/css2?family=Open+Sans:wght@400;600;700&display=swap" rel="stylesheet">
<style>
  :root {
    --page: #eef0f2;
    --brand-blue: #3f86d6;
    --brand-blue-light: #6aa6e6;
    --ink: #1e1e1e;
    --card-white: #ffffff;
    --card-black: #121212;
    --text-light: #e9e9e9;
    --text-muted: #bdbdbd;
  }
  * { margin: 0; padding: 0; box-sizing: border-box; }
  html, body { width: 1200px; height: 982px; overflow: hidden; }
  body {
    background: var(--page);
    font-family: "Open Sans", Arial, sans-serif;
    position: relative;
  }
  .card {
    position: absolute;
    width: 580px;
    height: 332px;
    border-radius: 18px;
    overflow: hidden;
    box-shadow: 0 6px 18px rgba(0,0,0,0.12);
  }

  /* Back of card */
  .card-back {
    left: 570px;
    top: 130px;
    background: linear-gradient(160deg, var(--brand-blue-light), var(--brand-blue));
  }
  .card-back .brand {
    position: absolute;
    left: 0; right: 0; top: 110px;
    text-align: center;
    color: var(--ink);
  }
  .brand-name {
    display: inline-flex;
    align-items: center;
    gap: 12px;
    font-weight: 600;
    font-size: 46px;
    letter-spacing: 1px;
    color: var(--ink);
  }
  .brand-dot {
    width: 14px; height: 14px; border-radius: 50%;
    background: var(--ink);
  }
  .brand-tagline {
    margin-top: 6px;
    font-size: 15px;
    font-weight: 400;
    color: var(--ink);
  }

  /* Front of card */
  .card-front {
    left: 50px;
    top: 520px;
    background: var(--card-white);
  }
  .card-front .wave {
    position: absolute; left: 0; top: 0;
  }
  .card-front .brand {
    position: absolute;
    left: 0; right: 0; top: 42px;
    text-align: center;
  }
  .card-front .brand-dot { background: var(--brand-blue); }
  .card-front .brand-name { font-size: 40px; }
  .card-front .brand-tagline { font-size: 13px; }

  .details {
    position: absolute;
    left: 0; right: 0; top: 218px;
    display: flex;
    justify-content: space-between;
    padding: 0 40px;
    color: var(--text-light);
    font-size: 11.5px;
    line-height: 1.6;
  }
  .clinic { padding-top: 6px; }
  .contact-name { font-weight: 700; font-size: 14px; color: #fff; }
  .credentials { color: var(--text-muted); margin-bottom: 4px; }
  .contact-line { display: flex; align-items: center; gap: 7px; }
  .contact-line svg { flex: none; }
  .contact-line svg path, .contact-line svg circle, .contact-line svg rect { stroke: var(--text-light); fill: none; stroke-width: 1.3; }
</style>
</head>
<body>

  <section class="card card-back" aria-label="Card back">
    <div class="brand">
      <div class="brand-name"><span class="brand-dot"></span>Bright Ferns</div>
      <p class="brand-tagline">Natural Wellness &amp; Live Cell Review</p>
    </div>
  </section>

  <section class="card card-front" aria-label="Card front">
    <svg class="wave" width="580" height="332" viewBox="0 0 580 332">
      <path d="M0,205 C140,150 330,150 580,178 L580,332 L0,332 Z" fill="var(--card-black)"/>
      <path d="M0,196 C140,140 330,140 580,168 L580,182 C330,156 140,158 0,208 Z" fill="var(--brand-blue)"/>
    </svg>

    <div class="brand">
      <div class="brand-name"><span class="brand-dot"></span>Bright Ferns</div>
      <p class="brand-tagline">Natural Wellness &amp; Live Cell Review</p>
    </div>

    <div class="details">
      <address class="clinic" style="font-style:normal">
        Larkvale Acupuncture Clinic<br>
        2736-18 Avenue, Suite 200<br>
        Larkvale, AB T8K 2P6
      </address>
      <div class="contact">
        <p class="contact-name">Marla Dunwoody</p>
        <p class="credentials">DynBC, CH, BA</p>
        <p class="contact-line">
          <svg width="12" height="12" viewBox="0 0 12 12"><path d="M3,1 L5,3 L4,5 C5,7 6,8 7,8 L9,7 L11,9 L9,11 C5,11 1,7 1,3 Z"/></svg>
          780.555.0148
        </p>
        <p class="contact-line">
          <svg width="12" height="12" viewBox="0 0 12 12"><rect x="1" y="2.5" width="10" height="7"/><path d="M1,2.5 L6,7 L11,2.5"/></svg>
          brightferns@mailnest.ca
        </p>
        <p class="contact-line">
          <svg width="12" height="12" viewBox="0 0 12 12"><circle cx="6" cy="6" r="5"/><path d="M1,6 H11 M6,1 C3,4 3,8 6,11 M6,1 C9,4 9,8 6,11"/></svg>
          www.brightfernsnaturalwellness.com
        </p>
      </div>
    </div>
  </section>

</body>
</html>
```